Hip / Cool Business Card for Custom Accessory Company

I would like to get a 2 sided design for standard size business cards, glossy (2 inches x 3.5 inches). Can be landscape or portrait layout! The design should include our logo (attached). The card should be extremely clear that the company is Tin Lantern. Should also have our URL clear. Should also use the color scheme seen on our upcoming site, tinlantern.example. The font we use is called "hurry up." Other than that, please go-to-town. We are targeting 15-45 y.o. market, with a skew on the 20-30 crowd. We do custom and stock iPhone cases as well as Cufflinks, Winestoppers; see the website for more.
Updates

Project Deadline Extended
Reason: Extending in case the US July 4th Holiday is keeping people from working!!

Industry/Entity Type

Landscape

Requirements
Must have
• Must be clear that the website is tinlantern.example. Must be clear that custom designs are an option.
Nice to have
• images of our designs. examples of our designs.
Should not have
• hard on the eyes contrasting colors such as orange on black. green on blue. Should not have any fonts that are considered "old" like Times New Roman. But decorative fonts are fine.

```html
<!DOCTYPE html>
<html lang="en">
<head>
<meta charset="utf-8">
<title>Tin Lantern — Business Card</title>
<link href="https://fonts.googleapis.com/css2?family=Lato:wght@400;700;900&display=swap" rel="stylesheet">
<style>
  :root {
    --stage: #3a3a3a;
    --paper: #ffffff;
    --teal: #17a0aa;
    --teal-light: #6fd0de;
    --teal-dark: #0f8f99;
    --ink: #111111;
    --text: #1e1e1e;
  }
  html, body { margin: 0; padding: 0; overflow: hidden; }
  body {
    width: 1200px; height: 750px;
    background: var(--stage);
    position: relative;
    font-family: "Lato", sans-serif;
  }
  .card {
    position: absolute;
    top: 212px;
    width: 519px; height: 295px;
    border-radius: 14px;
    background: var(--paper);
    overflow: hidden;
  }
  .card--front { left: 73px; }
  .card--back { left: 606px; }
  .card svg.backdrop { position: absolute; inset: 0; }

  .contact { position: absolute; left: 19px; top: 28px; color: var(--text); }
  .contact__name { margin: 0; font-size: 16px; font-weight: 700; color: var(--teal); line-height: 1.1; }
  .contact__role { margin: 2px 0 0; font-size: 12px; font-weight: 900; }
  .contact__address { margin: 14px 0 0; font-size: 12.5px; line-height: 15px; font-style: normal; }
  .contact__list { list-style: none; margin: 12px 0 0; padding: 0; font-size: 12.5px; line-height: 15.3px; }
  .contact__list li { display: flex; align-items: center; gap: 9px; }
  .contact__list svg { width: 13px; height: 12px; flex: none; }

  .wordmark {
    position: absolute; left: 258px; top: 38px;
    margin: 0; font-size: 29px; font-weight: 900;
    color: var(--ink); letter-spacing: 0.5px;
  }
  .mascot {
    position: absolute; border-radius: 50%;
    background: radial-gradient(circle at 40% 40%, #22b2bc, var(--teal-dark));
    border: 3px solid var(--ink);
  }
  .card--front .mascot { left: 343px; top: 88px; width: 126px; height: 126px; }
  .card--back .mascot {
    left: 46px; top: 8px; width: 282px; height: 282px;
    box-shadow: 0 0 0 5px var(--paper), 0 0 0 7px var(--ink);
  }

  .products {
    position: absolute; left: 364px; top: 80px;
    list-style: none; margin: 0; padding: 0;
    font-size: 16.5px; font-weight: 700; line-height: 20px; color: var(--ink);
  }
</style>
</head>
<body>

<section class="card card--front">
  <svg class="backdrop" viewBox="0 0 519 295" aria-hidden="true">
    <defs>
      <linearGradient id="wave-fill" x1="0" x2="1" y1="0" y2="0">
        <stop offset="0" stop-color="var(--teal)"/>
        <stop offset="0.5" stop-color="var(--teal-light)"/>
        <stop offset="1" stop-color="var(--teal)"/>
      </linearGradient>
    </defs>
    <path d="M0 220 C120 260 230 230 320 190 C400 160 470 160 519 172 L519 295 L0 295 Z" fill="url(#wave-fill)"/>
    <path d="M0 186 C40 200 70 250 150 246 C220 242 270 222 310 210 C265 232 215 252 150 254 C80 256 40 230 0 214 Z" fill="var(--ink)"/>
  </svg>

  <div class="contact">
    <h1 class="contact__name">Dara Quinn</h1>
    <p class="contact__role">Manager</p>
    <address class="contact__address">418B Alder Crest Lane Unit 207<br>Fernwick, VA 20990</address>
    <ul class="contact__list">
      <li><svg viewBox="0 0 13 12"><path d="M1 4 Q6.5 0 12 4 L10 5.5 L9 3.5 H4 L3 5.5 Z M3 6 H10 L11.5 11 H1.5 Z" fill="var(--teal)"/></svg>55501234</li>
      <li><svg viewBox="0 0 13 12"><rect x="3.5" y="0.5" width="6" height="11" rx="1.2" fill="none" stroke="var(--teal)" stroke-width="1.3"/></svg>+100 555 019</li>
      <li><svg viewBox="0 0 13 12"><rect x="0.5" y="1.5" width="12" height="9" fill="var(--teal)"/><path d="M0.5 1.5 L6.5 6.5 L12.5 1.5" fill="none" stroke="#fff" stroke-width="1.1"/></svg>support@tinlantern.example</li>
      <li><svg viewBox="0 0 13 12"><rect x="0.7" y="0.7" width="11.6" height="8" fill="none" stroke="var(--teal)" stroke-width="1.3"/><rect x="4" y="10" width="5" height="1.5" fill="var(--teal)"/></svg>www.tinlantern.example</li>
    </ul>
  </div>

  <p class="wordmark">TIN LANTERN</p>
  <div class="mascot" role="img" aria-label="Illustrated round teal brand mascot"></div>
</section>

<section class="card card--back">
  <svg class="backdrop" viewBox="0 0 519 295" aria-hidden="true">
    <path d="M210 0 H519 V295 H180 C280 240 300 80 210 0 Z" fill="var(--teal)"/>
  </svg>
  <div class="mascot" role="img" aria-label="Large illustrated round teal brand mascot"></div>
  <ul class="products">
    <li>Charm Bracelets</li>
    <li>Cufflinks</li>
    <li>Earrings</li>
    <li>Money Clips</li>
    <li>Necklaces</li>
    <li>Phone Cases</li>
    <li>Wine Stoppers</li>
  </ul>
</section>

</body>
</html>
```